Corporate PowerPoint Template

Seeking a Powerpoint Template Design for High Technology company based in Silicon Valley. We are seeking a general template design that conveys a professional, clean, progressive message.

The Template must have the following elements at a minimum:
1. Title Page (see comments following)
2. Agenda Page
3. Page Number, Date and Confidentiality Statement
Items in #3 are to appear on all pages except title page

We expect the Title page to be graphical in nature with area for Presentation Title, Presenter Name, Date and a place for confidentiality statement should be present as well. Three (3) distinct Title pages to address different constituencies: Customers, Partners and Internal Communications.

In general, we would like to stay with our corporate color scheme (which may be found in our logo). To better understand our products, logo and look and feel - please visit our website at: http://www.velmarotek.example

```html
<!DOCTYPE html>
<html lang="en">
<head>
<meta charset="utf-8">
<title>Velmarotek Presentation Template</title>
<link href="https://fonts.googleapis.com/css2?family=Didact+Gothic&family=Quicksand:wght@500;600;700&display=swap" rel="stylesheet">
<style>
  :root {
    --page-bg-top: #e3f3fb;
    --page-bg-bottom: #d3ecf8;
    --navy: #0b3a78;
    --royal: #0a56ad;
    --teal: #0d6b72;
    --teal-light: #148189;
    --brand-teal: #1a6e73;
    --brand-blue: #4a86c8;
    --ink: #1d1d1d;
    --muted: #8c8c8c;
    --white: #ffffff;
    --grey-light: #e6e6e6;
    --grey-mid: #9a9a9a;
    --grey-dark: #3c3c3c;
  }
  * { box-sizing: border-box; margin: 0; padding: 0; }
  html, body { width: 900px; height: 1200px; overflow: hidden; }
  body {
    background: linear-gradient(180deg, var(--page-bg-top), var(--page-bg-bottom));
    font-family: "Didact Gothic", "Century Gothic", sans-serif;
    position: relative;
  }
  .slide {
    position: absolute;
    left: 103px;
    width: 694px;
    height: 521px;
    background: var(--white);
    box-shadow: 0 2px 6px rgba(0,0,0,0.28);
    overflow: hidden;
  }
  .slide--title { top: 67px; }
  .slide--content {
    top: 613px;
    background: linear-gradient(160deg, #ffffff 55%, #eef0f6 100%);
  }

  /* Title slide */
  .title-top-band {
    position: absolute; left: 0; top: 0; width: 100%; height: 108px;
    background: linear-gradient(180deg, #0a2f66, var(--royal));
  }
  .hero-scene {
    position: absolute; left: 0; top: 108px; width: 100%; height: 278px;
    background:
      radial-gradient(ellipse 260px 120px at 88% 30%, #ffffff 0%, rgba(255,255,255,0) 70%),
      linear-gradient(180deg, #5d5d5d 0%, #c8c8c8 30%, #d9d9d9 48%, #6a6a6a 72%, #2e2e2e 100%);
    border-bottom: 2px solid #444;
  }
  .hero-stripe {
    position: absolute; left: 0; top: 243px; width: 100%; height: 62px;
    background: var(--royal);
  }
  .hero-inset {
    position: absolute; left: 65px; top: 186px; width: 184px; height: 172px;
    background: linear-gradient(180deg, #3a3a3a 0%, #8a8a8a 45%, #6e6e6e 55%, #2a2a2a 100%);
    box-shadow: 0 1px 4px rgba(0,0,0,0.5);
  }
  .hero-heading {
    position: absolute; left: 284px; top: 263px;
    font-family: "Quicksand", "Century Gothic", sans-serif;
    font-weight: 600; font-size: 16px; color: var(--white); letter-spacing: 0.2px;
  }
  .brand {
    position: absolute; display: flex; align-items: center;
    color: var(--brand-teal);
    font-family: "Quicksand", "Century Gothic", sans-serif; font-weight: 600;
  }
  .brand__dot { border-radius: 50%; background: var(--brand-blue); flex: none; }
  .brand--large { left: 38px; top: 425px; font-size: 36px; gap: 14px; }
  .brand--large .brand__dot { width: 50px; height: 50px; }
  .brand--small { left: 14px; top: 483px; font-size: 19px; gap: 7px; }
  .brand--small .brand__dot { width: 26px; height: 26px; }

  .footer-meta {
    position: absolute; top: 487px; left: 0; width: 100%;
    font-size: 11px; color: var(--muted);
  }
  .footer-meta__presenter { position: absolute; left: 244px; }
  .footer-meta__date { position: absolute; left: 527px; }
  .footer-meta__page { position: absolute; left: 647px; font-size: 9px; top: 2px; }

  /* Content slide */
  .content-header {
    position: absolute; left: 0; top: 0; width: 100%; height: 91px;
    background: linear-gradient(90deg, var(--teal), var(--teal-light));
    border-bottom: 2px solid #3a4a4c;
  }
  .content-title {
    position: absolute; left: 43px; top: 35px;
    font-family: "Quicksand", "Century Gothic", sans-serif;
    font-weight: 600; font-size: 27px; color: var(--white);
  }
  .confidential {
    position: absolute; right: 13px; top: 13px;
    font-size: 11px; color: var(--white);
  }
  .header-badge {
    position: absolute; left: 587px; top: 33px; width: 98px; height: 98px;
    border-radius: 50%; background: var(--white);
  }
  .content-body {
    position: absolute; left: 40px; top: 125px; width: 620px;
    font-size: 16.5px; line-height: 21px; color: var(--ink);
    list-style: none;
  }
  .content-body > li { position: relative; padding-left: 28px; margin-bottom: 28px; }
  .content-body > li::before { content: "•"; position: absolute; left: 2px; }
  .content-body ul { list-style: none; margin-top: 1px; }
  .content-body ul li { position: relative; padding-left: 30px; }
  .content-body ul li::before { content: "–"; position: absolute; left: 0; }
</style>
</head>
<body>

  <section class="slide slide--title" aria-label="Partners title slide">
    <div class="title-top-band"></div>
    <div class="hero-scene" role="img" aria-label="Monochrome photo of light streaks rushing through a tunnel"></div>
    <div class="hero-stripe"></div>
    <div class="hero-inset" role="img" aria-label="Close-up photo of a metal connector contact"></div>
    <h1 class="hero-heading">PARTNERS</h1>
    <div class="brand brand--large"><span class="brand__dot"></span>velmarotek</div>
    <div class="footer-meta">
      <span class="footer-meta__presenter">Presenter Name</span>
      <span class="footer-meta__date">30 August 2014</span>
      <span class="footer-meta__page">5</span>
    </div>
  </section>

  <section class="slide slide--content" aria-label="Text layout slide">
    <div class="content-header"></div>
    <h2 class="content-title">Text Layout</h2>
    <p class="confidential">Strictly Confidential</p>
    <div class="header-badge"></div>
    <ul class="content-body">
      <li>Lorem ipsum dolor sit amet, et pri vide fugit. Mel ea audiam percipit, eum bonorum menandri cotidieque ne.
        <ul>
          <li>Odio prodesset sea in, indoctum intellegebat in nec, at pri virtute ceteros nominati. Mucius option expetendis ei quo, te has elitr ornatus deseruisse. Et omnis latine concludaturque cum, his ad wisi assueverit appellantur.</li>
        </ul>
      </li>
      <li>Probo dicam causae an nec, ad pro altera postea.
        <ul>
          <li>Sed blandit omnesque reprehendunt in, aliquip propriae sit ex. Vis porro possim no, mucius apeirian temporibus pro in. Cum denique expetendis id. Vero deleniti ex mea.</li>
        </ul>
      </li>
    </ul>
    <div class="brand brand--small"><span class="brand__dot"></span>velmarotek</div>
    <div class="footer-meta">
      <span class="footer-meta__presenter">Presenter Name</span>
      <span class="footer-meta__date">30 August 2014</span>
      <span class="footer-meta__page">4</span>
    </div>
  </section>

</body>
</html>
```